TrueGrindz Complete Stationery - Logo already designed

I already have the logo designed see attached. I need have a full set of stationary and business card designed for printing. I have attached an example of what I mean.

Please feel free to be creative. Also you can use the X in the logo by its self if you think it will work.

My details:

Name: Corwin Lestak
Social media handles: @corwinlestak
W: corwinlestak.com
E: info@corwinlestak.com
​P: 08 7493 5286
PO Box 7382, Marlowe Bay 6142
ABN 83 402 719 265

Target Market(s)

Anyone looking to be inspired.

Industry/Entity Type

Business

Font styles to use
Sans Serif

Colors
fbee3e
000000

Requirements
Must have
• My details:
• Name: Corwin Lestak
• Social media handles: @corwinlestak
• W: corwinlestak.com
• E: info@corwinlestak.com
• ​P: 08 7493 5286
• PO Box 7382, Marlowe Bay 6142
• ABN 83 402 719 265
Nice to have
• Something a little different
Should not have
• must not look tacky.

```html
<!DOCTYPE html>
<html lang="en">
<head>
<meta charset="utf-8">
<title>TrueGrindz Business Card</title>
<link href="https://fonts.googleapis.com/css2?family=Barlow:wght@400;500;600;800&display=swap" rel="stylesheet">
<style>
  :root {
    --backdrop: #d9d9d9;
    --card: #2b2b2b;
    --card-edge: #333333;
    --ink: #f2f2f2;
    --ink-soft: #cfcfcf;
    --accent: #fbee3e;
    --accent-deep: #e6c400;
  }
  * { margin: 0; padding: 0; box-sizing: border-box; }
  html, body {
    width: 1200px; height: 900px; overflow: hidden;
    background: var(--backdrop);
    font-family: "Barlow", sans-serif;
  }
  .sheet {
    width: 1200px; height: 900px;
    display: flex; flex-direction: column;
    align-items: center; justify-content: center; gap: 44px;
  }
  .card {
    position: relative;
    width: 560px; height: 320px;
    background: linear-gradient(135deg, var(--card-edge), var(--card) 60%, #242424);
    border-radius: 3px;
    box-shadow: 0 10px 26px rgba(0,0,0,.28);
    color: var(--ink);
  }
  /* back side */
  .card-back .social-handle {
    position: absolute; left: 44px; bottom: 40px;
    font-size: 15px; font-weight: 400; letter-spacing: .04em;
    color: var(--ink-soft);
  }
  /* front side */
  .brand {
    position: absolute; left: 40px; top: 50%; transform: translateY(-50%);
    display: flex; align-items: center; gap: 10px;
  }
  .brand-mark {
    width: 14px; height: 14px; border-radius: 50%;
    background: var(--accent);
  }
  .brand-name {
    font-size: 38px; font-weight: 800; letter-spacing: -.01em;
    color: var(--ink); text-transform: uppercase;
  }
  .divider {
    position: absolute; left: 302px; top: 40px;
    width: 2px; height: 240px;
    background: linear-gradient(to bottom, transparent, var(--accent-deep) 20%, var(--accent-deep) 80%, transparent);
  }
  .details {
    position: absolute; left: 330px; top: 52px; right: 24px;
  }
  .person-name {
    font-size: 21px; font-weight: 600; letter-spacing: .05em;
    margin-bottom: 20px; margin-left: 12px;
  }
  .contact-list { list-style: none; margin-left: 4px; }
  .contact-list li {
    display: flex; align-items: center; gap: 6px;
    font-size: 15px; font-weight: 400; letter-spacing: .04em;
    line-height: 22px; color: var(--ink);
  }
  .contact-list svg { width: 13px; height: 13px; flex: none; }
  .address {
    margin-top: 12px; font-style: normal;
    font-size: 16px; letter-spacing: .06em; line-height: 22px;
    color: var(--ink-soft);
  }
  .abn {
    margin-top: 10px;
    font-size: 15px; font-weight: 500; letter-spacing: .03em;
    color: var(--accent);
  }
</style>
</head>
<body>
<main class="sheet">
  <section class="card card-back" aria-label="Card back">
    <p class="social-handle">@corwinlestak</p>
  </section>

  <section class="card card-front" aria-label="Card front">
    <div class="brand">
      <span class="brand-mark"></span>
      <span class="brand-name">TrueGrindz</span>
    </div>
    <div class="divider"></div>
    <div class="details">
      <h1 class="person-name">Corwin Lestak</h1>
      <ul class="contact-list">
        <li>
          <svg viewBox="0 0 16 16" aria-hidden="true"><path fill="#fbee3e" d="M3.6 1.5l2.3 2.6-1.3 1.8c.9 2 2.5 3.6 4.5 4.5l1.8-1.3 2.6 2.3-1.2 2.1C7.5 13.5 2.5 8.5 1.5 2.7z"/></svg>
          <span>: 08 7493 5286</span>
        </li>
        <li>
          <svg viewBox="0 0 16 16" aria-hidden="true"><rect x="1" y="3.5" width="14" height="9" rx="1" fill="#fbee3e"/><path d="M1.5 4l6.5 5 6.5-5" fill="none" stroke="#2b2b2b" stroke-width="1.2"/></svg>
          <span>: info@corwinlestak.com</span>
        </li>
        <li>
          <svg viewBox="0 0 16 16" aria-hidden="true"><circle cx="8" cy="8" r="6.5" fill="none" stroke="#fbee3e" stroke-width="1.5"/><ellipse cx="8" cy="8" rx="2.6" ry="6.5" fill="none" stroke="#fbee3e" stroke-width="1.2"/><path d="M1.5 8h13" stroke="#fbee3e" stroke-width="1.2"/></svg>
          <span>: corwinlestak.com</span>
        </li>
      </ul>
      <address class="address">PO Box 7382<br>Marlowe Bay 6142</address>
      <p class="abn">ABN 83 402 719 265</p>
    </div>
  </section>
</main>
</body>
</html>
```